Business Card Design Project

New Business Card design for Varodine Technology Ltd using new Logo and new Tagline for staffing company.

About us from our website - www.varodine.example:

VaroDine is a leading and recognized Electronic Entertainment, Workforce Augmentation, and Project Management solutions provider with clients in Electronic Entertainment, Legal, Technology, Government and other verticals that range in size from start up organizations to Zenlar 500 companies. VaroDine is certified as an 8(a) minority and woman owned enterprise, established in 1998.

Target Market(s)

Companies in Electronic Entertainment, Legal, Government and Technology

Industry/Entity Type

Business

Requirements
Must have
• Must include in small letters the following information on back:

Established in 1998
8(a)(w)(e), Cage #7KRT9, DUNS #462137580

Front should have the following:
Derek Holloway
Vice President
5820 Birchmont Road
Fallowby, FB 482917
555-318-2746 X 100
555-902-6613 Fax
555-318-2746 Toll Free
name@varodine.example

Our Tagline: Link • Build • Deliver

```html
<!DOCTYPE html>
<html lang="en">
<head>
<meta charset="utf-8">
<title>VaroDine Business Card</title>
<link rel="stylesheet" href="https://fonts.googleapis.com/css2?family=Arimo:wght@400;700&display=swap">
<style>
  :root {
    --backdrop: #dcdde2;
    --card-black: #050505;
    --brand-blue: #2a68bf;
    --ink-white: #ffffff;
    --ink-soft: #d9d9d9;
  }
  * { margin: 0; padding: 0; box-sizing: border-box; }
  html, body {
    width: 1200px;
    height: 768px;
    overflow: hidden;
    background: var(--backdrop);
    font-family: "Arimo", Arial, sans-serif;
  }
  .canvas {
    width: 1200px;
    height: 768px;
    display: flex;
    align-items: center;
    justify-content: center;
    gap: 80px;
  }
  .card {
    position: relative;
    width: 350px;
    height: 600px;
    background: var(--card-black);
    overflow: hidden;
    box-shadow: 0 6px 18px rgba(0,0,0,0.25);
    color: var(--ink-white);
  }
  .card-arc {
    position: absolute;
    inset: 0;
    width: 100%;
    height: 100%;
  }
  .card-arc .band {
    fill: none;
    stroke: var(--brand-blue);
    stroke-width: 44;
  }
  .wordmark {
    position: absolute;
    left: 0;
    right: 0;
    text-align: center;
    font-weight: 700;
    color: var(--ink-white);
    letter-spacing: -0.5px;
  }
  .card-front .wordmark {
    top: 444px;
    font-size: 50px;
  }
  .tagline {
    position: absolute;
    top: 18px;
    left: 0;
    right: 0;
    text-align: center;
    font-weight: 700;
    font-size: 15px;
  }
  .card-back .wordmark {
    top: 64px;
    font-size: 26px;
  }
  .contact {
    position: absolute;
    left: 26px;
    top: 228px;
    font-size: 16px;
    line-height: 1.2;
    color: var(--ink-white);
  }
  .contact .address { margin-top: 18px; }
  .credentials {
    position: absolute;
    left: 26px;
    bottom: 34px;
    font-size: 10.5px;
    line-height: 1.35;
    color: var(--ink-soft);
  }
</style>
</head>
<body>
<main class="canvas">
  <section class="card card-front" aria-label="Card front">
    <svg class="card-arc" viewBox="0 0 350 600" aria-hidden="true">
      <circle class="band" cx="-90" cy="600" r="440"/>
    </svg>
    <div class="wordmark">VaroDine</div>
  </section>

  <section class="card card-back" aria-label="Card back">
    <svg class="card-arc" viewBox="0 0 350 600" aria-hidden="true">
      <ellipse class="band" cx="100" cy="620" rx="250" ry="480"/>
    </svg>
    <p class="tagline">Link • Build • Deliver</p>
    <div class="wordmark">VaroDine</div>
    <div class="contact">
      <p class="person">Derek Holloway<br>Vice President</p>
      <p class="phones">555-318-2746 X 100<br>555-902-6613 Fax<br>555-318-2746 Toll Free<br>name@varodine.example</p>
      <p class="address">5820 Birchmont Road<br>Fallowby, FB 482917</p>
    </div>
    <p class="credentials">Established in 1998<br>8(a)(w)(e), Cage #7KRT9, DUNS #462137580</p>
  </section>
</main>
</body>
</html>
```